KV Group

We need a new website for our company and since we had a very good work done for our logo in this site, we're back for the entire job.

Our company name is Marlowe Capital Group. We're adding files of examples of what we have done today. In my opinion we need a more attention lock in the site but yet financial simple work.

Our files (attached) will let you know what we have so far. We need a complete change but the colours should be the same, however you can change them not running away to far from the original, and of course matching with the logo.

We need examples for 3 kind of layouts.

- A HOME welcome layout
- An internal Layout with sidebar
- And internal Layout wide

We can buy image licenses if needed for assets.
Actually there are 5 slide images placed on the Welcome HOME, we need those there, but you can improve with better images to match the new website!!!

Target Market(s)

Clients looking for financial advisers, tax and funds specialist, currency advisers

Industry/Entity Type

Financial

Requirements
Must have
• all the fonts must be in accordance with the financial market sites........the welcome home page must be precise, neat and information accurate........the menu should be elegant........main focus on the Home page, should be also the PRIVATE ACCESS box log in.......

```html
<!DOCTYPE html>
<html lang="en">
<head>
<meta charset="utf-8">
<title>Marlowe Capital Group</title>
<link rel="stylesheet" href="https://fonts.googleapis.com/css2?family=Source+Sans+3:wght@400;600;700&family=Oswald:wght@400;500&display=swap">
<style>
:root{
  --orange:#f47b20;
  --dark:#262626;
  --black:#0b0b0b;
  --ink:#222;
  --muted:#8a8a8a;
  --paper:#f4f4f2;
  --white:#fff;
  --line:#e1e1e1;
  --seal:#d6d6d4;
  --green:#1c8a1c;
  --red:#d42020;
  --navy:#1c2a5a;
}
*{box-sizing:border-box;margin:0;padding:0}
html,body{width:668px;height:1200px;overflow:hidden}
body{position:relative;background:var(--paper);font-family:"Source Sans 3",Arial,sans-serif;color:var(--ink)}
.abs{position:absolute}

.topbar{left:0;top:0;width:668px;height:23px;background:var(--dark)}
.toplink{top:6px;font-size:9px;color:#eee;letter-spacing:.2px;display:flex;align-items:center;gap:5px}
.toplink svg{width:9px;height:9px}

.header{left:0;top:23px;width:668px;height:91px;background:linear-gradient(#f8f8f8,#d9d9d9);border-bottom:2px solid var(--orange)}
.brand{left:67px;top:66px;display:flex;align-items:center;gap:6px}
.brand-mark{width:14px;height:14px;background:var(--orange)}
.brand-name{font-size:14px;font-weight:600;color:var(--ink);letter-spacing:.3px}
.nav{left:235px;top:79px;width:366px;display:flex;justify-content:space-between;font-size:8.5px;color:#333}
.nav span{white-space:nowrap}
.nav .active{color:var(--orange);border-bottom:1.5px solid var(--orange);padding-bottom:2px}

.slider{left:67px;top:104px;width:534px;height:222px;background:linear-gradient(120deg,#c9ccd0 0%,#8e9196 40%,#b7bcc2 70%,#e6e6e6 100%)}
.slide-arrow{top:222px;width:20px;height:20px;border-radius:50%;background:rgba(40,40,40,.75);display:flex;align-items:center;justify-content:center}
.caption{left:338px;top:195px;width:230px;height:88px;background:rgba(40,40,40,.82);padding:12px 10px 0}
.caption h2{font-weight:400;font-size:16px;color:var(--orange);margin-bottom:4px}
.caption p{font-size:8.5px;line-height:12.5px;color:#eee}

.access{left:67px;top:330px;width:534px;height:45px;background:var(--orange)}
.access-label{left:67px;top:330px;width:133px;height:45px;background:var(--black);color:var(--white);font-size:15px;padding:13px 0 0 12px;clip-path:polygon(0 0,128px 0,133px 50%,128px 100%,0 100%)}
.field{top:343px;width:137px;height:19px;background:var(--white);border:1px solid #ddd}
.login{left:503px;top:343px;width:86px;height:19px;background:var(--black);color:var(--white);font-size:8px;text-align:center;line-height:19px}

.welcome{left:67px;top:395px;width:534px;text-align:center}
.welcome h1{font-weight:400;font-size:16px;margin-bottom:8px}
.welcome h1 em{font-style:normal;color:var(--orange)}
.welcome p{font-size:8px;line-height:12px;color:#444}

.card{top:484px;width:160px;height:265px;background:var(--white);border:1px solid var(--line);padding:10px 9px}
.card-head{display:flex;align-items:flex-start;gap:8px;height:46px}
.card-num{font-family:"Oswald",sans-serif;font-size:32px;color:#888;line-height:1}
.card-title{font-family:"Oswald",sans-serif;color:var(--orange);line-height:1.05}
.card-title small{display:block;font-size:11px}
.card-title b{display:block;font-size:17px;font-weight:500}
.card-img{width:142px;height:84px}
.card p{font-size:7.8px;line-height:12.5px;margin-top:10px;color:#222}
.more{position:absolute;left:11px;bottom:12px;background:var(--orange);color:var(--white);font-size:8px;padding:5px 6px}

.ticker{left:67px;top:772px;width:534px;height:22px;background:#f8f8f6;border:1px solid var(--line);display:flex;align-items:center;justify-content:space-around;font:700 6.5px Verdana,sans-serif;color:var(--navy);white-space:nowrap;overflow:hidden}
.up{color:var(--green)}.down{color:var(--red)}.flat{color:#e0a000}

.verified{left:67px;top:822px;width:534px;text-align:center;font-size:11px;color:var(--orange)}
.verified-rule{left:67px;top:832px;width:534px;height:1px;background:var(--line)}
.seals{left:67px;top:858px;width:534px;display:flex;justify-content:center;gap:40px}
.seal{width:70px;height:26px;background:var(--seal);border-radius:3px}

.footer{left:0;top:913px;width:668px;height:169px;background:var(--dark)}
.fcol{top:938px;font-size:6.8px;line-height:12.2px;color:#8c8c8c;white-space:nowrap}
.fcol h4{font-size:8px;font-weight:600;color:#eee;padding-bottom:5px;border-bottom:1px solid #3e3e3e;margin-bottom:5px}
.bottom{left:0;top:1082px;width:668px;height:118px;background:var(--black)}
.disclaimer{left:67px;top:1096px;width:534px;text-align:center;color:#3d3d3d;font-size:6.5px;line-height:12px}
.disclaimer h5{font-size:8px;color:#555;margin-bottom:2px}
.bottom-rule{left:67px;top:1167px;width:534px;height:1px;background:#2a2a2a}
.copy{left:67px;top:1181px;width:534px;text-align:center;font-size:7px;color:#555}
</style>
</head>
<body>

<div class="abs topbar"></div>
<div class="abs toplink" style="left:465px"><svg viewBox="0 0 10 10"><rect x="1" y="1" width="8" height="8" fill="none" stroke="#ddd"/><line x1="3" y1="4" x2="7" y2="4" stroke="#ddd"/><line x1="3" y1="6" x2="7" y2="6" stroke="#ddd"/></svg>APPLY NOW</div>
<div class="abs toplink" style="left:541px"><svg viewBox="0 0 10 10"><rect x="1" y="2" width="8" height="6" fill="#ddd"/><path d="M1 2 L5 5 L9 2" fill="none" stroke="#444"/></svg>CONTACT US</div>

<header class="abs header"></header>
<div class="abs brand"><span class="brand-mark"></span><span class="brand-name">Marlowe Capital Group</span></div>
<nav class="abs nav">
  <span class="active">HOME</span><span>ABOUT US ▾</span><span>INVESTMENTS ▾</span><span>FUNDS ▾</span><span>BROKERAGE ▾</span><span>EXCHANGE ▾</span><span>ACCOUNTS ▾</span>
</nav>

<div class="abs slider" role="img" aria-label="Photo of a team of bankers meeting around a table"></div>
<div class="abs slide-arrow" style="left:72px"><svg width="8" height="8" viewBox="0 0 8 8"><path d="M5.5 1 L2.5 4 L5.5 7" fill="none" stroke="#fff" stroke-width="1.5"/></svg></div>
<div class="abs slide-arrow" style="left:577px"><svg width="8" height="8" viewBox="0 0 8 8"><path d="M2.5 1 L5.5 4 L2.5 7" fill="none" stroke="#fff" stroke-width="1.5"/></svg></div>
<div class="abs caption">
  <h2>Teamwork for your benifit</h2>
  <p>Our dedicated Private Bankers, will proactively keep you up to date with relevant information and provide a financial overview that enables you to make better decisions.</p>
</div>

<div class="abs access"></div>
<div class="abs access-label">PRIVATE ACCESS</div>
<div class="abs field" style="left:212px"></div>
<div class="abs field" style="left:358px"></div>
<div class="abs login">LOG IN TO ACCOUNT</div>

<section class="abs welcome">
  <h1>Welcome to <em>Marlowe Capital Group</em></h1>
  <p>Lorem ipsum dolor sit amet, consectetur adipiscing elit. Nulla lobortis consequat mauris, eget eleifend nunc viverra viverra. Ut ac risus odio. Aliquam pretium purus sed nulla feugiat blandit. Cras vel libero ut lacus eleifend tempor. Phasellus eleifend, magna non tincidunt accumsan, justo arcu cursus ipsum, non porttitor sapien quam vel magna. Maecenas elit nisl, molestie nec dapibus nec, aliquet a erat.</p>
</section>

<article class="abs card" style="left:67px">
  <div class="card-head"><span class="card-num">1.</span><span class="card-title"><small>MANAGEMENT</small><b>&amp; STRATEGY</b></span></div>
  <div class="card-img" role="img" aria-label="Photo of advisers reviewing documents at a desk" style="background:linear-gradient(135deg,#6b6e72,#c9ccd0)"></div>
  <p>Lorem ipsum dolor sit amet, consectetur adipiscing elit. Nulla lobortis consequat mauris, eget eleifend nunc viverra viverra. Ut ac risus odio. Aliquam pretium purus sed nulla feugiat blandit.</p>
  <span class="more">Read More</span>
</article>
<article class="abs card" style="left:254px">
  <div class="card-head"><span class="card-num">2.</span><span class="card-title"><small>OUR</small><b>FUNDS</b></span></div>
  <div class="card-img" role="img" aria-label="Photo of a piggy bank on a stack of banknotes" style="background:linear-gradient(#f3f3f3,#e8c9c9 60%,#a9a48a)"></div>
  <p>Lorem ipsum dolor sit amet, consectetur adipiscing elit. Nulla lobortis consequat mauris, eget eleifend nunc viverra viverra. Ut ac risus odio. Aliquam pretium purus sed nulla feugiat blandit.</p>
  <span class="more">Read More</span>
</article>
<article class="abs card" style="left:441px">
  <div class="card-head"><span class="card-num">3.</span><span class="card-title"><small>CURRENCY</small><b>EXCHANGE</b></span></div>
  <div class="card-img" role="img" aria-label="Photo of mixed international banknotes" style="background:linear-gradient(135deg,#b9a27c,#8ea77e 50%,#c9b48f)"></div>
  <p>Lorem ipsum dolor sit amet, consectetur adipiscing elit. Nulla lobortis consequat mauris, eget eleifend nunc viverra viverra. Ut ac risus odio. Aliquam pretium purus sed nulla feugiat blandit.</p>
  <span class="more">Read More</span>
</article>

<div class="abs ticker">
  <span class="up">▲</span>
  <span>GBP/UAH = <span class="up">12.65761 ▲</span></span>
  <span>GBP/UGX = <span class="down">4010.06174 ▼</span></span>
  <span>GBP/USD = <span class="up">1.55817 ▲</span></span>
  <span>GBP/UYU = <span class="up">34.36026 ▲</span></span>
  <span>GBP/VEF = <span class="flat">0</span></span>
  <span>GBP/VUV = <span class="up">151.</span></span>
</div>

<div class="abs verified-rule"></div>
<div class="abs verified"><span style="background:var(--paper);padding:0 8px">Verified and Protected by</span></div>
<div class="abs seals" role="img" aria-label="Partner verification seals">
  <span class="seal"></span><span class="seal"></span><span class="seal"></span><span class="seal"></span>
</div>

<footer class="abs footer"></footer>
<div class="abs fcol" style="left:67px;width:50px"><h4>About Us</h4>History<br>Expertize<br>Identity<br>Strategy<br>Contact Us</div>
<div class="abs fcol" style="left:163px;width:120px"><h4>Investments</h4>Term Deposits<br>Management &amp; Strategy<br>Client Relations<br>Financial Privacy<br>Tax Advice<br>Wealth Analysis &amp; Financial Planning<br>Active Advisory Group<br>Manager Selection Services<br>Private Equity</div>
<div class="abs fcol" style="left:313px;width:78px"><h4>Funds</h4>Overview<br>Administration<br>Funds Security<br>Core Services<br>Reporting<br>Revenue Opportunities<br>How it works?<br>Glossary</div>
<div class="abs fcol" style="left:429px;width:68px"><h4>Currency Exchange</h4>Foreign Exchange<br>Fx Forword<br>Fx Options</div>
<div class="abs fcol" style="left:429px;top:1006px;width:50px"><h4>Accounts</h4>Apply Now<br>Private Access</div>
<div class="abs fcol" style="left:552px;width:49px"><h4>Brokerage</h4>Institutional<br>Research<br>Trading</div>

<div class="abs bottom"></div>
<div class="abs disclaimer">
  <h5>Disclaimer</h5>
  Lorem ipsum dolor sit amet, consectetur adipiscing elit. Nulla lobortis consequat mauris, eget eleifend nunc viverra viverra. Ut ac risus odio. Aliquam pretium purus sed nulla feugiat blandit. Cras vel libero ut lacus eleifend tempor. Phasellus eleifend, magna non tincidunt accumsan, justo arcu cursus ipsum, non porttitor sapien quam vel magna. Maecenas elit nisl, molestie nec dapibus nec, aliquet a erat. Donec scelerisque lacus a libero suscipit auctor volutpat enim euismod. Mauris porta, lacus ut ullamcorper sodales, mauris tortor feugiat purus, nec aliquam neque purus ac metus. Nunc eleifend leo quis nisl hendrerit ultrices. Suspendisse quis feugiat elit.
</div>
<div class="abs bottom-rule"></div>
<div class="abs copy">© 2013 Marlowe Capital Group All right reserved.</div>

</body>
</html>
```